Bref créative
Olive Oil and Balsamic Vinegar Company
Lomisca
- I am looking for a modern label for my Olive oil and Balsamics.
- The parameter for the label is 2" by 4"
- I want a classic looking but edgey label. The bottled cost 23.99 so it has to show time was spend into the design.
- They are imported from Italy so i need some resemblence to italy but not the green, red, white color scheme.
- The name of the oils "Lomisca" i want in a cursive type writing but with the "F" to be a bigger with loop type font you can say.
Food
Im a wholeseller and a personal seller so i have a wind target of customer from corporate to normal day people.
I need to be able to edit the texts so i can add history and change the name of the flavors.
Contact me if need clarification or more details
Example 2 I really like
Example 1 I really like

```html
<!DOCTYPE html>
<html lang="en">
<head>
<meta charset="utf-8">
<title>Lomisca label concepts</title>
<link href="https://fonts.googleapis.com/css2?family=Cormorant+Garamond:ital,wght@0,400;1,400;1,600&family=Great+Vibes&family=Kaushan+Script&family=Alex+Brush&family=Pinyon+Script&family=Italianno&family=Parisienne&family=Playball&family=Dancing+Script:wght@600&family=Mr+De+Haviland&display=swap" rel="stylesheet">
<style>
:root{
  --page:#ffffff;
  --rule:#d6d6d6;
  --ink:#1a1a1a;
  --label-dark:#14110b;
  --label-mid:#2a2316;
  --gold:#c9a54a;
  --gold-light:#ecd58e;
  --cream:#f4efe2;
  --olive-dark:#3b3410;
  --olive:#8a7a1c;
  --olive-light:#c4a932;
}
*{box-sizing:border-box;margin:0;padding:0}
html,body{width:1200px;height:686px;overflow:hidden;background:var(--page)}
.board{position:relative;width:1200px;height:686px;font-family:"Cormorant Garamond",serif;color:var(--ink)}
.panel{position:absolute;width:358px;height:228px;border-bottom:1px solid var(--rule)}
.panel.col-a{left:0;border-right:1px solid var(--rule)}
.panel.col-b{left:361px;border-right:1px solid var(--rule)}
.row-1{top:0}.row-2{top:229px}.row-3{top:458px}
.panel-title{position:absolute;top:4px;left:0;width:100%;text-align:center;font-style:italic;font-weight:600;font-size:13px}
.col-b .panel-title{left:-60px}
.item{position:absolute}
.label{background:linear-gradient(135deg,var(--label-mid),var(--label-dark) 60%);border:2px solid var(--gold);box-shadow:inset 0 0 0 3px var(--label-dark),inset 0 0 0 4px var(--gold);display:flex;flex-direction:column;align-items:center;justify-content:center;color:var(--cream);overflow:hidden}
.label.oval{border-radius:50%}
.brand{font-size:30px;line-height:1;color:var(--cream);white-space:nowrap}
.tagline{font-style:italic;font-size:9px;color:var(--gold-light);margin-top:2px;white-space:nowrap}
.label.small .brand{font-size:12px}
.label.oval.mid .brand{font-size:20px}
.label.large .brand{font-size:38px}
.label.large .tagline{font-size:11px}
.bottle{background:linear-gradient(90deg,var(--olive-dark),var(--olive) 40%,var(--olive-light) 55%,var(--olive-dark));border-radius:40% 40% 6px 6px / 18% 18% 6px 6px}
.bottle.mini{background:linear-gradient(90deg,#2a2418,#5a4a30 50%,#2a2418);border-radius:30% 30% 4px 4px / 12% 12% 4px 4px}
.gift-box{background:linear-gradient(90deg,#e9e6dd,#fbfaf6 50%,#dcd8cc);border:1px solid #cfc9b8}
.note{position:absolute;font-style:italic;font-size:9px;white-space:nowrap}
.font-1 .brand{font-family:"Great Vibes",cursive}
.font-2 .brand{font-family:"Kaushan Script","Playball",cursive}
.font-3 .brand{font-family:"Alex Brush",cursive}
.font-4 .brand{font-family:"Pinyon Script","Great Vibes",cursive}
.font-5 .brand{font-family:"Italianno",cursive}
.font-6 .brand{font-family:"Parisienne",cursive}
.font-2 .label .brand{font-size:26px}
.font-2 .label.small .brand{font-size:10px}
.font-2 .label.oval.mid .brand{font-size:17px}
.font-2 .label.large .brand{font-size:32px}
.font-4 .label .brand{font-size:26px}
.font-4 .label.small .brand{font-size:10px}
.font-4 .label.oval.mid .brand{font-size:17px}
.font-4 .label.large .brand{font-size:32px}
.font-5 .label .brand{font-size:38px}
.font-5 .label.small .brand{font-size:15px}
.font-5 .label.oval.mid .brand{font-size:28px}
.font-5 .label.large .brand{font-size:46px}
.font-intro{position:absolute;left:955px;top:175px;width:150px;text-align:center;font-style:italic;font-size:11px;line-height:1.3}
.font-list{position:absolute;left:920px;top:270px;list-style:none}
.font-list li{display:flex;align-items:center;height:40px}
.sample{width:140px;font-size:28px;line-height:1;white-space:nowrap}
.sample-name{font-size:12px}
.s1{font-family:"Playball",cursive}
.s2{font-family:"Dancing Script",cursive}
.s3{font-family:"Kaushan Script","Playball",cursive}
.s4{font-family:"Great Vibes",cursive}
.s5{font-family:"Italianno",cursive;font-size:32px}
.s6{font-family:"Mr De Haviland",cursive;font-size:32px}
</style>
</head>
<body>
<main class="board">

<section class="panel col-a row-1 font-1">
  <h2 class="panel-title">Previous designs same font</h2>
  <div class="item label" style="left:10px;top:30px;width:140px;height:76px"><span class="brand">Lomisca</span><span class="tagline">Olive Oil and Balsamics</span></div>
  <div class="item bottle mini" role="img" aria-label="Small dark bottle with label" style="left:160px;top:30px;width:18px;height:72px"></div>
  <div class="item label oval small" style="left:188px;top:32px;width:46px;height:70px"><span class="brand">Lomisca</span></div>
  <div class="item gift-box" role="img" aria-label="White gift box with bottle" style="left:246px;top:30px;width:36px;height:76px"></div>
  <div class="item bottle" role="img" aria-label="Olive oil bottle with label" style="left:298px;top:24px;width:42px;height:196px"></div>
  <div class="item label oval mid" style="left:10px;top:126px;width:84px;height:52px"><span class="brand">Lomisca</span></div>
  <div class="item bottle mini" role="img" aria-label="Small dark bottle with label" style="left:102px;top:120px;width:20px;height:80px"></div>
  <div class="item label large" style="left:132px;top:118px;width:156px;height:86px"><span class="brand">Lomisca</span><span class="tagline">Olive Oil and Balsamics</span></div>
</section>

<section class="panel col-b row-1 font-2">
  <h2 class="panel-title">Thicker font</h2>
  <div class="item label" style="left:10px;top:26px;width:130px;height:70px"><span class="brand">Lomisca</span><span class="tagline">Olive Oil and Balsamics</span></div>
  <p class="note" style="left:10px;top:98px">Thicker font</p>
  <div class="item bottle mini" role="img" aria-label="Small dark bottle with label" style="left:150px;top:26px;width:18px;height:68px"></div>
  <div class="item label oval small" style="left:176px;top:28px;width:44px;height:66px"><span class="brand">Lomisca</span></div>
  <p class="note" style="left:176px;top:98px">Thicker font</p>
  <div class="item gift-box" role="img" aria-label="White gift box with bottle" style="left:232px;top:20px;width:34px;height:74px"></div>
  <p class="note" style="left:232px;top:4px">Thicker font</p>
  <div class="item bottle" role="img" aria-label="Olive oil bottle with label" style="left:296px;top:24px;width:42px;height:180px"></div>
  <p class="note" style="left:296px;top:208px">Thicker font</p>
  <div class="item label oval mid" style="left:10px;top:122px;width:80px;height:50px"><span class="brand">Lomisca</span></div>
  <p class="note" style="left:10px;top:176px">Thicker font</p>
  <div class="item bottle mini" role="img" aria-label="Small dark bottle with label" style="left:98px;top:118px;width:20px;height:78px"></div>
  <div class="item label large" style="left:128px;top:116px;width:156px;height:84px"><span class="brand">Lomisca</span><span class="tagline">Olive Oil and Balsamics</span></div>
  <p class="note" style="left:190px;top:208px">Thicker font</p>
</section>

<section class="panel col-a row-2 font-3">
  <h2 class="panel-title">Previous designs with new font</h2>
  <div class="item label" style="left:10px;top:30px;width:140px;height:76px"><span class="brand">Lomisca</span><span class="tagline">Olive Oil and Balsamics</span></div>
  <div class="item bottle mini" role="img" aria-label="Small dark bottle with label" style="left:160px;top:30px;width:18px;height:72px"></div>
  <div class="item label oval small" style="left:188px;top:32px;width:46px;height:70px"><span class="brand">Lomisca</span></div>
  <div class="item gift-box" role="img" aria-label="White gift box with bottle" style="left:246px;top:30px;width:36px;height:76px"></div>
  <div class="item bottle" role="img" aria-label="Olive oil bottle with label" style="left:298px;top:24px;width:42px;height:196px"></div>
  <div class="item label oval mid" style="left:10px;top:126px;width:84px;height:52px"><span class="brand">Lomisca</span></div>
  <div class="item bottle mini" role="img" aria-label="Small dark bottle with label" style="left:102px;top:120px;width:20px;height:80px"></div>
  <div class="item label large" style="left:132px;top:118px;width:156px;height:86px"><span class="brand">Lomisca</span><span class="tagline">Olive Oil and Balsamics</span></div>
</section>

<section class="panel col-b row-2 font-4">
  <h2 class="panel-title">Previous designs with new font</h2>
  <div class="item label" style="left:10px;top:30px;width:140px;height:76px"><span class="brand">Lomisca</span><span class="tagline">Olive Oil and Balsamics</span></div>
  <div class="item bottle mini" role="img" aria-label="Small dark bottle with label" style="left:160px;top:30px;width:18px;height:72px"></div>
  <div class="item label oval small" style="left:188px;top:32px;width:46px;height:70px"><span class="brand">Lomisca</span></div>
  <div class="item gift-box" role="img" aria-label="White gift box with bottle" style="left:246px;top:30px;width:36px;height:76px"></div>
  <div class="item bottle" role="img" aria-label="Olive oil bottle with label" style="left:298px;top:24px;width:42px;height:196px"></div>
  <div class="item label oval mid" style="left:10px;top:126px;width:84px;height:52px"><span class="brand">Lomisca</span></div>
  <div class="item bottle mini" role="img" aria-label="Small dark bottle with label" style="left:102px;top:120px;width:20px;height:80px"></div>
  <div class="item label large" style="left:132px;top:118px;width:156px;height:86px"><span class="brand">Lomisca</span><span class="tagline">Olive Oil and Balsamics</span></div>
</section>

<section class="panel col-a row-3 font-5">
  <h2 class="panel-title">Previous designs with new font</h2>
  <div class="item label" style="left:10px;top:30px;width:140px;height:76px"><span class="brand">Lomisca</span><span class="tagline">Olive Oil and Balsamics</span></div>
  <div class="item bottle mini" role="img" aria-label="Small dark bottle with label" style="left:160px;top:30px;width:18px;height:72px"></div>
  <div class="item label oval small" style="left:188px;top:32px;width:46px;height:70px"><span class="brand">Lomisca</span></div>
  <div class="item gift-box" role="img" aria-label="White gift box with bottle" style="left:246px;top:30px;width:36px;height:76px"></div>
  <div class="item bottle" role="img" aria-label="Olive oil bottle with label" style="left:298px;top:24px;width:42px;height:196px"></div>
  <div class="item label oval mid" style="left:10px;top:126px;width:84px;height:52px"><span class="brand">Lomisca</span></div>
  <div class="item bottle mini" role="img" aria-label="Small dark bottle with label" style="left:102px;top:120px;width:20px;height:80px"></div>
  <div class="item label large" style="left:132px;top:118px;width:156px;height:86px"><span class="brand">Lomisca</span><span class="tagline">Olive Oil and Balsamics</span></div>
</section>

<section class="panel col-b row-3 font-6">
  <h2 class="panel-title">Previous designs with new font</h2>
  <div class="item label" style="left:10px;top:30px;width:140px;height:76px"><span class="brand">Lomisca</span><span class="tagline">Olive Oil and Balsamics</span></div>
  <div class="item bottle mini" role="img" aria-label="Small dark bottle with label" style="left:160px;top:30px;width:18px;height:72px"></div>
  <div class="item label oval small" style="left:188px;top:32px;width:46px;height:70px"><span class="brand">Lomisca</span></div>
  <div class="item gift-box" role="img" aria-label="White gift box with bottle" style="left:246px;top:30px;width:36px;height:76px"></div>
  <div class="item bottle" role="img" aria-label="Olive oil bottle with label" style="left:298px;top:24px;width:42px;height:196px"></div>
  <div class="item label oval mid" style="left:10px;top:126px;width:84px;height:52px"><span class="brand">Lomisca</span></div>
  <div class="item bottle mini" role="img" aria-label="Small dark bottle with label" style="left:102px;top:120px;width:20px;height:80px"></div>
  <div class="item label large" style="left:132px;top:118px;width:156px;height:86px"><span class="brand">Lomisca</span><span class="tagline">Olive Oil and Balsamics</span></div>
</section>

<p class="font-intro">These are some cursive writing fonts examples with names</p>
<ul class="font-list">
  <li><span class="sample s1">Lomisca</span><span class="sample-name">Dealer Hand</span></li>
  <li><span class="sample s2">Lomisca</span><span class="sample-name">Corvella</span></li>
  <li><span class="sample s3">Lomisca</span><span class="sample-name">Freestroke 40</span></li>
  <li><span class="sample s4">Lomisca</span><span class="sample-name">Harwick</span></li>
  <li><span class="sample s5">Lomisca</span><span class="sample-name">Jaskeri</span></li>
  <li><span class="sample s6">Lomisca</span><span class="sample-name">Mirolant</span></li>
</ul>

</main>
</body>
</html>
```